Stationery Design Project

We are looking for a full revision of our existing stationary to include within this project:

- Letterhead
- Business card
- Compliment slip

The items should be a reflection of our new website which can be found at http://www.brackenledger.co.uk/

Our logo files are included within the file brief

There are some further projects which we may approach the winning designer for as we need a revision to the front cover of our reports, a new price list and two brochures for specific target markets.

Industry/Entity Type

Business

```html
<!DOCTYPE html>
<html lang="en">
<head>
<meta charset="utf-8">
<title>Bracken Ledger — Stationery</title>
<link rel="stylesheet" href="https://fonts.googleapis.com/css2?family=Open+Sans:wght@400;600&display=swap">
<style>
  :root{
    --stage:#ebe7e2;
    --paper:#f4f4f6;
    --brand-blue:#1d50a4;
    --brand-navy:#28287a;
    --ink-grey:#8c8c94;
    --ink-light:#c4c4ca;
    --white:#ffffff;
  }
  *{box-sizing:border-box;margin:0;padding:0}
  html,body{width:1200px;height:957px;overflow:hidden}
  body{background:var(--stage);font-family:"Open Sans",Arial,sans-serif;position:relative}

  .sheet{position:absolute;background:var(--paper);box-shadow:0 2px 10px rgba(0,0,0,.18);overflow:hidden}
  .sheet svg.band{position:absolute;inset:0;width:100%;height:100%}

  .wordmark{position:absolute;display:flex;align-items:center;gap:8px;font-weight:600;color:var(--brand-navy);letter-spacing:.04em;text-transform:uppercase;white-space:nowrap}
  .wordmark .mark-dot{width:10px;height:10px;background:var(--brand-navy)}
  .wordmark.on-blue{color:var(--white)}
  .wordmark.on-blue .mark-dot{background:var(--white)}

  .contact{position:absolute;list-style:none}
  .contact li{display:flex;align-items:center;gap:6px;color:var(--ink-grey);white-space:nowrap}
  .contact svg{flex:none}

  /* letterhead */
  .letterhead{left:640px;top:40px;width:500px;height:707px}
  .letterhead .wordmark{left:120px;top:62px;font-size:27px}
  .letterhead .contact{left:140px;top:598px}
  .letterhead .contact li{font-size:9px;margin-bottom:8px;color:var(--ink-light)}
  .letterhead .swoosh{position:absolute;left:140px;top:672px;width:320px;height:14px}

  /* compliment slip */
  .comp-slip{left:50px;top:70px;width:560px;height:264px}
  .comp-slip .wordmark{left:28px;top:30px;font-size:25px}
  .comp-slip .greeting{position:absolute;left:90px;top:96px;font-size:13px;color:var(--ink-light)}
  .comp-slip .company{position:absolute;left:28px;top:156px;font-size:8px;font-weight:600;color:var(--brand-navy)}
  .comp-slip .address{position:absolute;left:28px;top:168px;font-size:8px;color:var(--ink-grey)}
  .comp-slip .contact{left:28px;top:181px;display:flex;gap:26px}
  .comp-slip .contact li{font-size:6.5px}

  /* business cards */
  .card{width:330px;height:200px}
  .card-front{left:50px;top:480px}
  .card-front .wordmark{left:0;right:0;justify-content:center;top:84px;font-size:25px}
  .card-back{left:50px;top:730px;background:var(--brand-blue)}
  .card-back .wordmark{left:24px;top:30px;font-size:19px}
  .card-back .contact{left:24px;top:140px}
  .card-back .contact li{font-size:7px;color:var(--white);margin-bottom:5px}
</style>
</head>
<body>

<section class="sheet letterhead" aria-label="Letterhead">
  <svg class="band" viewBox="0 0 500 707" preserveAspectRatio="none" aria-hidden="true">
    <path d="M0 0H72C40 90 44 220 70 330C96 450 70 560 118 612L96 707H0Z" fill="var(--brand-blue)"/>
    <path d="M72 0C40 90 44 220 70 330C96 450 70 560 118 612L96 707" fill="none" stroke="var(--white)" stroke-width="6"/>
  </svg>
  <div class="wordmark"><span class="mark-dot"></span>Bracken Ledger</div>
  <ul class="contact">
    <li><svg width="26" height="18" viewBox="0 0 26 18"><rect x="1" y="1" width="24" height="16" fill="none" stroke="var(--ink-light)" stroke-width="2"/><path d="M1 1L13 10L25 1" fill="none" stroke="var(--ink-light)" stroke-width="2"/></svg>mail@brackenledger.co.uk</li>
    <li><svg width="26" height="22" viewBox="0 0 26 22"><rect x="1" y="1" width="24" height="20" rx="3" fill="none" stroke="var(--ink-light)" stroke-width="2"/><path d="M8 5C7 11 12 17 18 17L19 14L16 12L14 13C12 12 10 10 10 8L11 6L9 4Z" fill="var(--ink-light)"/></svg>01632 960 418</li>
    <li><svg width="26" height="26" viewBox="0 0 26 26"><circle cx="13" cy="13" r="11" fill="none" stroke="var(--ink-light)" stroke-width="2"/><path d="M2 13H24M13 2C7 8 7 18 13 24M13 2C19 8 19 18 13 24" fill="none" stroke="var(--ink-light)" stroke-width="1.5"/></svg>http://www.brackenledger.co.uk/</li>
  </ul>
  <svg class="swoosh" viewBox="0 0 320 14" preserveAspectRatio="none" aria-hidden="true"><path d="M0 12C100 4 220 2 320 2" fill="none" stroke="var(--ink-light)" stroke-width="1.5"/></svg>
</section>

<section class="sheet comp-slip" aria-label="Compliment slip">
  <svg class="band" viewBox="0 0 560 264" preserveAspectRatio="none" aria-hidden="true">
    <path d="M0 196C120 240 300 252 470 244L560 222V264H0Z" fill="var(--brand-blue)"/>
    <path d="M0 196C120 240 300 252 470 244L560 222" fill="none" stroke="var(--white)" stroke-width="4"/>
  </svg>
  <div class="wordmark"><span class="mark-dot"></span>Bracken Ledger</div>
  <p class="greeting">With Compliments of</p>
  <p class="company">brackenledger</p>
  <p class="address">14 Mill Lane, Harrowgate Park, Leeds LS1 4QR.</p>
  <ul class="contact">
    <li><svg width="9" height="7" viewBox="0 0 9 7"><rect width="9" height="7" fill="var(--brand-blue)"/><path d="M0 0L4.5 4L9 0" fill="none" stroke="var(--white)"/></svg>mail@brackenledger.co.uk</li>
    <li><svg width="8" height="8" viewBox="0 0 8 8"><rect width="8" height="8" rx="1.5" fill="var(--brand-blue)"/><path d="M2.5 2C2 4 3.5 6 5.5 6L6 5L5 4.2L4.4 4.6C3.8 4.2 3.4 3.8 3.3 3.2L3.8 2.6L3 1.6Z" fill="var(--white)"/></svg>01632 960 418</li>
    <li><svg width="8" height="8" viewBox="0 0 8 8"><circle cx="4" cy="4" r="3.5" fill="none" stroke="var(--brand-blue)"/><path d="M0.5 4H7.5M4 0.5V7.5" stroke="var(--brand-blue)" stroke-width=".7"/></svg>http://www.brackenledger.co.uk/</li>
  </ul>
</section>

<section class="sheet card card-front" aria-label="Business card, front">
  <div class="wordmark"><span class="mark-dot"></span>Bracken Ledger</div>
</section>

<section class="sheet card card-back" aria-label="Business card, back">
  <svg class="band" viewBox="0 0 330 200" preserveAspectRatio="none" aria-hidden="true">
    <path d="M222 0C250 60 236 140 262 200H330V0Z" fill="var(--paper)"/>
    <path d="M222 0C250 60 236 140 262 200" fill="none" stroke="var(--white)" stroke-width="3"/>
  </svg>
  <div class="wordmark on-blue"><span class="mark-dot"></span>Bracken Ledger</div>
  <ul class="contact">
    <li><svg width="9" height="7" viewBox="0 0 9 7"><rect x=".5" y=".5" width="8" height="6" fill="none" stroke="var(--white)"/><path d="M.5 .5L4.5 4L8.5 .5" fill="none" stroke="var(--white)"/></svg>mail@brackenledger.co.uk</li>
    <li><svg width="8" height="8" viewBox="0 0 8 8"><rect x=".5" y=".5" width="7" height="7" rx="1.5" fill="none" stroke="var(--white)"/><path d="M2.5 2C2 4 3.5 6 5.5 6L6 5L5 4.2L4.4 4.6C3.8 4.2 3.4 3.8 3.3 3.2L3.8 2.6L3 1.6Z" fill="var(--white)"/></svg>01632 960 418</li>
    <li><svg width="8" height="8" viewBox="0 0 8 8"><circle cx="4" cy="4" r="3.5" fill="none" stroke="var(--white)"/><path d="M0.5 4H7.5M4 0.5V7.5" stroke="var(--white)" stroke-width=".7"/></svg>http://www.brackenledger.co.uk/</li>
  </ul>
</section>

</body>
</html>
```